Wattlegrove Campus Lodgings needs a business card design

Hi Guys,

We are a Student Accommodation company in Australia. We already have a logo which I will submit.

I will require the design of the business cards from you.

I am after something that looks clean, modern and that people feel interested and actually want to contact us.

We would like to see designs that are innovative.

On the business cards I will require to have:

Employee Name
Position
Phone number
Email
Facebook page

I hope you can help me with this project guys as I have heard really good things from you.

```html
<!DOCTYPE html>
<html lang="en">
<head>
<meta charset="utf-8">
<title>Wattlegrove Campus Lodgings – Business Card</title>
<link rel="stylesheet" href="https://fonts.googleapis.com/css2?family=Exo+2:wght@400;500;600;700&display=swap">
<style>
  :root {
    --page-bg: #e9eaec;
    --card-white: #ffffff;
    --card-shade: #e4e5e7;
    --brand-green: #0b9419;
    --brand-yellow: #f2b31b;
    --ink: #2b2b2b;
    --ink-soft: #3d3d3d;
  }
  * { box-sizing: border-box; margin: 0; padding: 0; }
  html, body {
    width: 1200px; height: 900px; overflow: hidden;
    background: var(--page-bg);
    font-family: "Exo 2", sans-serif;
  }
  .stage {
    width: 1200px; height: 900px;
    display: flex; align-items: center; justify-content: center;
  }
  .card {
    position: relative;
    width: 1050px; height: 600px;
    border-radius: 44px;
    overflow: hidden;
    background: radial-gradient(ellipse at 52% 38%, var(--card-white) 0%, #f6f6f7 45%, var(--card-shade) 100%);
    box-shadow: 0 14px 40px rgba(0,0,0,.18);
  }
  .card__waves { position: absolute; inset: 0; width: 100%; height: 100%; }

  .brand {
    position: absolute; left: 70px; top: 215px;
    display: flex; align-items: center; gap: 14px;
  }
  .brand__mark { width: 38px; height: 38px; background: var(--brand-green); }
  .brand__name {
    font-weight: 700; font-size: 30px; line-height: 1.05;
    color: var(--brand-green); letter-spacing: .5px; text-transform: uppercase;
  }

  .person {
    position: absolute; right: 120px; top: 62px; text-align: right;
  }
  .person__name {
    font-size: 28px; font-weight: 600; letter-spacing: 2px;
    color: var(--ink); text-transform: uppercase;
  }
  .person__role {
    font-size: 17px; font-weight: 500; letter-spacing: 1.5px;
    color: var(--ink-soft); text-transform: uppercase;
  }

  .contacts {
    position: absolute; right: 78px; top: 158px;
    list-style: none; text-align: right;
  }
  .contacts__item {
    display: flex; align-items: center; justify-content: flex-end; gap: 12px;
    font-size: 17px; letter-spacing: 1.5px; color: var(--ink);
    height: 30px;
  }
  .contacts__icon { width: 20px; height: 20px; fill: none; stroke: var(--ink); stroke-width: 1.8; }
  .contacts__item--plain { font-size: 15px; letter-spacing: 1px; }

  .address {
    position: absolute; left: 72px; top: 392px;
    font-size: 22px; font-weight: 500; letter-spacing: 1.5px; line-height: 1.45;
    color: var(--ink);
  }
</style>
</head>
<body>
<main class="stage">
  <article class="card">
    <svg class="card__waves" viewBox="0 0 1050 600" preserveAspectRatio="none" aria-hidden="true">
      <path fill="var(--brand-green)" d="M0 480 C 260 535, 560 480, 790 385 C 910 335, 990 290, 1050 250 L1050 600 L0 600 Z"/>
      <path fill="var(--brand-yellow)" d="M320 478 C 600 455, 850 370, 1050 195 L1050 232 C 860 385, 610 462, 320 478 Z"/>
    </svg>

    <div class="brand">
      <span class="brand__mark"></span>
      <span class="brand__name">Wattlegrove<br>Campus Lodgings</span>
    </div>

    <header class="person">
      <h1 class="person__name">Ellis Harrow</h1>
      <p class="person__role">President</p>
    </header>

    <ul class="contacts">
      <li class="contacts__item">021 555 0147
        <svg class="contacts__icon" viewBox="0 0 24 24"><path d="M5 3h4l2 5-2.5 1.5a11 11 0 0 0 6 6L16 13l5 2v4a2 2 0 0 1-2 2A16 16 0 0 1 3 5a2 2 0 0 1 2-2z"/></svg>
      </li>
      <li class="contacts__item">021 555 0148
        <svg class="contacts__icon" viewBox="0 0 24 24"><rect x="7" y="2" width="10" height="20" rx="2"/><line x1="11" y1="18" x2="13" y2="18"/></svg>
      </li>
      <li class="contacts__item">021 555 0149
        <svg class="contacts__icon" viewBox="0 0 24 24"><rect x="4" y="9" width="16" height="11" rx="1"/><rect x="8" y="3" width="8" height="6"/><line x1="8" y1="14" x2="16" y2="14"/></svg>
      </li>
      <li class="contacts__item contacts__item--plain">ellis@wattlegrove.au
        <svg class="contacts__icon" viewBox="0 0 24 24"><rect x="3" y="5" width="18" height="14" rx="1"/><path d="M3 6l9 7 9-7"/></svg>
      </li>
      <li class="contacts__item contacts__item--plain">www.wattlegrove.au
        <svg class="contacts__icon" viewBox="0 0 24 24"><circle cx="12" cy="12" r="9"/><ellipse cx="12" cy="12" rx="4" ry="9"/><line x1="3" y1="12" x2="21" y2="12"/></svg>
      </li>
    </ul>

    <address class="address" style="font-style: normal;">
      41 Level 9, Arcade<br>Ferncourt Road NSW
    </address>
  </article>
</main>
</body>
</html>
```